Wohnhof am Weiher - Zeitungsinserat für den Verkauf von Eigentumswohnungen

Wir brauchen ein Zeitungsinserat in zwei Formaten. Einmal 296 Breite x 440 Höhe mm und einmal 296 Breite x 220 mm Höhe.
Als Basis dient der sehr grobe Entwurf im Powerpoint (Entwurf.pptx).
Auf dem Entwurf fehlen noch die Kontaktangeben:
Brunnhofer Liegenschaften AG
Seematteweg 14
4387 Tannried
079 462 37 58
rbrunnhofer@tessin-ostwald.ch

Zudem muss noch der Link auf die Webseite aufgeführt werden.
www.wohnhof-am-weiher.ch

Zudem fehlt noch der Text:
Fordern Sie noch heute die Verkaufsunterlagen gedruckt oder per Email an. Schreiben Sie uns einfach eine Chatpost mit Ihrer Adresse.

Ich habe noch Files von den Innenvisualisierungen, den Aussenvisualisierungen sowie unser Logo hinzugefügt. Zudem habe ich Ihnen die Verkaufsbrochure angefügt. Sie können die Daten vom Entwurf gerne ergänzen wenn Ihnen etwas gefällt. Schön wäre es, wenn Sie den Stil ähnlich machen würden wie die Brochure.

Target Market(s)

Famillien, Paare und Rentner

Font styles to use
Serif

Colors

Designer to choose colors to be used in the design.

Requirements
Must have
• Tolles Design das sofort anspricht!

```html
<!DOCTYPE html>
<html lang="de">
<head>
<meta charset="utf-8">
<title>Wohnhof am Weiher – Inserat</title>
<link href="https://fonts.googleapis.com/css2?family=Montserrat:wght@400;500;700&family=Roboto+Condensed:wght@400;700&display=swap" rel="stylesheet">
<style>
:root{
  --blue:#0b6a96;
  --red:#e01b22;
  --ink:#1a1a1a;
  --frame:#dfe6e9;
  --line:#d6dde1;
  --page:#ececec;
  --paper:#ffffff;
}
*{box-sizing:border-box;margin:0;padding:0}
html,body{width:1200px;height:1200px;overflow:hidden;background:var(--page)}
.ad{position:absolute;left:0;top:154px;width:1200px;height:892px;background:var(--paper);overflow:hidden;font-family:'Montserrat',sans-serif;color:var(--ink)}
.hero{position:absolute;left:0;top:0}
.title{position:absolute;left:36px;top:44px;font-size:47px;font-weight:700;color:var(--blue);letter-spacing:-0.5px;line-height:1}
.subtitle{position:absolute;left:38px;top:98px;font-size:17.5px;font-weight:500;color:var(--red)}
.brand{position:absolute;right:24px;top:52px;text-align:right;color:var(--blue);font-weight:700;font-size:22px;line-height:1.15;letter-spacing:1px}
.features{position:absolute;left:35px;top:148px;display:flex;flex-direction:column;gap:6px}
.feature{display:flex}
.feature svg{width:37px;height:37px;flex:none;margin-top:3px}
.feature .txt{margin-left:14px}
.feature h3{font-size:14.5px;font-weight:700;color:var(--blue);line-height:16px;white-space:nowrap}
.feature p{font-size:9px;line-height:11.6px;margin-top:1px}
.thumb{position:absolute;top:476px;width:177px;height:100px;border:1.5px solid var(--red);background:linear-gradient(180deg,#f4f4f2 0%,#dcdad6 60%,#b9b4ad 100%)}
.house{position:absolute;top:587px;width:353px}
.tab{margin-left:53px;width:247px;height:39px;background:var(--blue);border-radius:6px 6px 0 0;color:#fff;font-weight:700;font-size:28px;text-align:center;line-height:40px}
.tab-foot{margin-left:53px;width:247px;height:8px;background:var(--blue);border-radius:0 0 5px 5px}
table{width:353px;table-layout:fixed;border-collapse:separate;border-spacing:0;font-family:'Roboto Condensed',sans-serif;font-size:10.5px;background:#fff;border:1px solid var(--line);border-radius:5px;overflow:hidden}
th{background:var(--red);color:#fff;font-weight:700;font-size:13px;line-height:12px;height:34px;border-right:1px solid #fff;text-align:center}
th small{font-size:8.5px;display:block;line-height:10px}
td{border-right:1px solid var(--line);border-top:1px solid var(--line);padding:0 2px;line-height:12px;vertical-align:middle}
th:last-child,td:last-child{border-right:none}
td.c{text-align:center;white-space:nowrap}
tr.r1 td{height:27px}tr.r2 td{height:24px}tr.r3 td{height:46px}tr.r4 td{height:46px}
.contact{position:absolute;top:839px;left:0;width:100%;height:36px;font-family:'Roboto Condensed',sans-serif}
.contact .ico{position:absolute;top:0;width:34px;height:34px;border:2px solid var(--blue);border-radius:6px;display:flex;align-items:center;justify-content:center}
.contact .ico svg{width:20px;height:20px}
.contact .val{position:absolute;color:var(--ink);white-space:nowrap}
.addr{left:164px;top:1px;font-size:12.5px;line-height:16px}
.phone{left:382px;top:3px;font-size:21px;font-weight:700}
.mail{left:562px;top:5px;font-size:17px}
.web{left:872px;top:5px;font-size:17px}
.rule{position:absolute;left:111px;top:887px;width:978px;height:5px;background:var(--blue)}
</style>
</head>
<body>
<div class="ad">
  <svg class="hero" width="1200" height="892" viewBox="0 0 1200 892">
    <defs>
      <linearGradient id="scene" x1="0" y1="0" x2="0" y2="1">
        <stop offset="0" stop-color="#7fa7cf"/>
        <stop offset="0.35" stop-color="#c9dbe9"/>
        <stop offset="0.52" stop-color="#d9d9d4"/>
        <stop offset="0.66" stop-color="#8c9a7a"/>
        <stop offset="0.78" stop-color="#5f9a3a"/>
        <stop offset="1" stop-color="#3f7d26"/>
      </linearGradient>
    </defs>
    <polygon points="635,0 1200,250 1200,580 189,580" fill="var(--frame)"/>
    <polygon role="img" aria-label="Aussenvisualisierung der Wohnanlage mit drei Häusern, Wiese und Bäumen" points="640,28 1176,260 1176,556 215,556" fill="url(#scene)"/>
  </svg>

  <h1 class="title">Wohnhof am Weiher</h1>
  <p class="subtitle">Hochwertige und moderne Eigentumswohnungen</p>
  <div class="brand">BRUNNHOFER<br>LIEGENSCHAFTEN AG</div>

  <div class="features">
    <div class="feature">
      <svg viewBox="0 0 40 40"><circle cx="19" cy="21" r="16" fill="none" stroke="var(--blue)" stroke-width="2.6"/><path d="M10 20l7 8L35 4" fill="none" stroke="var(--red)" stroke-width="6" stroke-linecap="round" stroke-linejoin="round"/></svg>
      <div class="txt" style="width:350px"><h3>Bus und Bahn</h3><p>Der Bahnhof von Grünau mit Zugverbindungen nach Rheinstadt (20 Minuten) und Juraville ist in wenigen Minuten mit dem Bus zu erreichen.</p></div>
    </div>
    <div class="feature">
      <svg viewBox="0 0 40 40"><circle cx="19" cy="21" r="16" fill="none" stroke="var(--blue)" stroke-width="2.6"/><path d="M10 20l7 8L35 4" fill="none" stroke="var(--red)" stroke-width="6" stroke-linecap="round" stroke-linejoin="round"/></svg>
      <div class="txt" style="width:330px"><h3>Einkaufen und weitere Dienstleistungen</h3><p>Durch die Nähe der Gemeindegrenze zwischen Grünau und Tannried liegen die Dorfzentren mit ihren Einkaufsmöglichkeiten (z.B. Talmarkt Center Grünau sowie der Altstadt in Grünau) und Dienstleistungsangeboten in max. 2 Minuten Fahrtzeit oder in 10-15 Minuten Gehdistanz.</p></div>
    </div>
    <div class="feature">
      <svg viewBox="0 0 40 40"><circle cx="19" cy="21" r="16" fill="none" stroke="var(--blue)" stroke-width="2.6"/><path d="M10 20l7 8L35 4" fill="none" stroke="var(--red)" stroke-width="6" stroke-linecap="round" stroke-linejoin="round"/></svg>
      <div class="txt" style="width:280px"><h3>Autobahn</h3><p>Die Wohnsiedlung ist ideal auch für den Individualverkehr erschlossen. Die Entfernung zur Autobahn A18 beträgt 12km und ist über Eichbach innerhalb von 15 Minuten erreichbar.</p></div>
    </div>
    <div class="feature">
      <svg viewBox="0 0 40 40"><circle cx="19" cy="21" r="16" fill="none" stroke="var(--blue)" stroke-width="2.6"/><path d="M10 20l7 8L35 4" fill="none" stroke="var(--red)" stroke-width="6" stroke-linecap="round" stroke-linejoin="round"/></svg>
      <div class="txt" style="width:225px"><h3>Rheinstadt</h3><p>Der nahegelegene Bahnhof in Grünau verfügt über sehr gute Verbindungen nach Rheinstadt (20 Minuten), welche durch den Doppelspurausbau in den kommenden Jahren sogar noch weiter verbessert werden.</p></div>
    </div>
    <div class="feature">
      <svg viewBox="0 0 40 40"><circle cx="19" cy="21" r="16" fill="none" stroke="var(--blue)" stroke-width="2.6"/><path d="M10 20l7 8L35 4" fill="none" stroke="var(--red)" stroke-width="6" stroke-linecap="round" stroke-linejoin="round"/></svg>
      <div class="txt" style="width:165px"><h3>Erholung im Grünen</h3><p>Tannried erfüllt mit seinen Wäldern, dem eigenen Weiherberg, dem Föhrenkopf, den offenen Feldern, den Wander- und Velorouten und der ländlichen Ruhe alle Voraussetzungen, die ein Naherholungsgebiet begehrt machen.</p></div>
    </div>
  </div>

  <div class="thumb" style="left:304px" role="img" aria-label="Innenvisualisierung Wohnzimmer mit Essbereich"></div>
  <div class="thumb" style="left:488px" role="img" aria-label="Innenvisualisierung Küche mit Esstisch"></div>
  <div class="thumb" style="left:674px" role="img" aria-label="Innenvisualisierung offener Wohn- und Essbereich"></div>
  <div class="thumb" style="left:858px" role="img" aria-label="Innenvisualisierung Küche mit Kochinsel"></div>

  <section class="house" style="left:53px">
    <div class="tab">Haus A</div>
    <table>
      <colgroup><col style="width:75px"><col style="width:62px"><col style="width:47px"><col style="width:95px"><col></colgroup>
      <tr><th>Attika</th><th>4.5<br>Zimmer</th><th>108m²</th><th>105m²<small>Sonnenterrasse</small></th><th>945'000<br>CHF</th></tr>
      <tr class="r1"><td>Obergeschoss</td><td>3.5 Zimmer</td><td class="c">81m²</td><td class="c">16m2 Balkon</td><td class="c">754'800 CHF</td></tr>
      <tr class="r2"><td>Obergeschoss</td><td>4.5 Zimmer</td><td class="c">102m²</td><td class="c">33m2 Balkon</td><td class="c">640'000 CHF</td></tr>
      <tr class="r3"><td>Erdgeschoss</td><td>3.5 Zimmer</td><td class="c">81m²</td><td>16m² gedeckter<br>Sitzplatz &amp;<br>eigener Garten</td><td class="c">657'000 CHF</td></tr>
      <tr class="r4"><td>Erdgeschoss</td><td>4.5 Zimmer</td><td class="c">102m²</td><td>33m² gedeckter<br>Sitzplatz &amp;<br>eigener Garten</td><td class="c">765'000 CHF</td></tr>
    </table>
    <div class="tab-foot"></div>
  </section>

  <section class="house" style="left:425px">
    <div class="tab">Haus B</div>
    <table>
      <colgroup><col style="width:75px"><col style="width:62px"><col style="width:47px"><col style="width:95px"><col></colgroup>
      <tr><th>Attika</th><th>4.5<br>Zimmer</th><th>109m²</th><th>107m²<small>Sonnenterrasse</small></th><th>965'000<br>CHF</th></tr>
      <tr class="r1"><td>Obergeschoss</td><td>3.5 Zimmer</td><td class="c">69m²</td><td class="c">14m² Balkon</td><td class="c">550'000 CHF</td></tr>
      <tr class="r2"><td>Obergeschoss</td><td>4.5 Zimmer</td><td class="c">117m²</td><td class="c">42m² Balkon</td><td class="c">877'500 CHF</td></tr>
      <tr class="r3"><td>Erdgeschoss</td><td>3.5 Zimmer</td><td class="c">69m²</td><td>14m² gedeckter<br>Sitzplatz &amp;<br>eigener Garten</td><td class="c">560'000 CHF</td></tr>
      <tr class="r4"><td>Erdgeschoss</td><td>4.5 Zimmer</td><td class="c">117m²</td><td>42m² gedeckter<br>Sitzplatz &amp;<br>eigener Garten</td><td class="c">889'000 CHF</td></tr>
    </table>
    <div class="tab-foot"></div>
  </section>

  <section class="house" style="left:792px">
    <div class="tab">Haus C</div>
    <table>
      <colgroup><col style="width:75px"><col style="width:62px"><col style="width:47px"><col style="width:95px"><col></colgroup>
      <tr><th>Attika</th><th>4.5<br>Zimmer</th><th>108m²</th><th>132m²<small>Sonnenterrasse</small></th><th>945'000<br>CHF</th></tr>
      <tr class="r1"><td>Obergeschoss</td><td>5.5 Zimmer</td><td class="c">143m²</td><td class="c">16m² Balkon</td><td class="c">1'058'000 CHF</td></tr>
      <tr class="r2"><td>Obergeschoss</td><td>3.5 Zimmer</td><td class="c">96m²</td><td class="c">23m² Balkon</td><td class="c">730'000 CHF</td></tr>
      <tr class="r3"><td>Erdgeschoss</td><td>5.5 Zimmer</td><td class="c">143m²</td><td>43m² gedeckter<br>Sitzplatz &amp;<br>eigener Garten</td><td class="c">1'065'000 CHF</td></tr>
      <tr class="r4"><td>Erdgeschoss</td><td>3.5 Zimmer</td><td class="c">96m²</td><td>23m² gedeckter<br>Sitzplatz &amp;<br>eigener Garten</td><td class="c">740'000 CHF</td></tr>
    </table>
    <div class="tab-foot"></div>
  </section>

  <div class="contact">
    <div class="ico" style="left:120px"><svg viewBox="0 0 24 24"><path d="M12 2a7 7 0 0 0-7 7c0 5 7 13 7 13s7-8 7-13a7 7 0 0 0-7-7z" fill="none" stroke="var(--blue)" stroke-width="2.2"/><circle cx="12" cy="9" r="2.6" fill="var(--blue)"/></svg></div>
    <div class="val addr">Brunnhofer Liegenschaften AG,<br>Seematteweg 14, 4387 Tannried</div>
    <div class="ico" style="left:338px"><svg viewBox="0 0 24 24"><path d="M6.6 2.5l3 3.6-1.8 2.4a12 12 0 0 0 7.7 7.7l2.4-1.8 3.6 3-1.9 3.3C12 21 3 12 3.3 4.4z" fill="var(--blue)"/></svg></div>
    <div class="val phone">079 462 37 58</div>
    <div class="ico" style="left:516px"><svg viewBox="0 0 24 24"><rect x="3" y="6" width="18" height="12" rx="1" fill="var(--blue)"/><path d="M3.5 6.8L12 13l8.5-6.2" fill="none" stroke="#fff" stroke-width="1.6"/></svg></div>
    <div class="val mail">rbrunnhofer@tessin-ostwald.ch</div>
    <div class="ico" style="left:828px"><svg viewBox="0 0 24 24" fill="none" stroke="var(--blue)" stroke-width="1.7"><circle cx="12" cy="12" r="9"/><ellipse cx="12" cy="12" rx="4" ry="9"/><path d="M3 12h18M4.5 7.5h15M4.5 16.5h15"/></svg></div>
    <div class="val web">www.wohnhof-am-weiher.ch</div>
  </div>
  <div class="rule"></div>
</div>
</body>
</html>
```